Bramble Harbor Foundation Web Design

The design we need is for a WordPress blog that will be our content platform. We are a registered 501(c)3 non-profit that focuses on financially supporting the treatment of cancer patients that have been told they have no hope and there is nothing the conventional medical system can do for them. Through this wesbite we want to both rasie awareness about the treatment options plus, raise funds for treating patients. The two primary target audiences of the site are...

1. Terminally ill patients and their families to let them know that there is an option other then hospice and that we are hear to support that option.

2. People looking to help donate to a worthwhile cause that resonates with them.

The website is https://brambleharborfoundation.org/

See attached logo designs!!!

Target Market(s)

Cancer patients and their families

Industry/Entity Type

Foundation

Font styles to use
Sans Serif

Colors
ffffff
fbed22

Requirements
Must have
• I like this look of this site. It is clean, simple, helpful, soft. I like the flow of the pages.
• http://www.quietmeadowtrust.org/
• I like the design and flow but NOT the color or boldness
• https://tmvq-youth.org/
• I like this style for a donation page.
• https://www.curewaveaid.org/about-cwa/stand-with-us/gifts/single-gift
• with the addition of a Would you like your employer to match? button.
Nice to have
• White black and gold - but soft
• Even possibly grayscale like the site I like.

```html
<!DOCTYPE html>
<html lang="en">
<head>
<meta charset="utf-8">
<title>Bramble Harbor Foundation</title>
<link href="https://fonts.googleapis.com/css2?family=Lato:ital,wght@0,300;0,400;0,700;1,400&display=swap" rel="stylesheet">
<style>
:root{
  --gold:#ecc84f;
  --gold-soft:#f1d978;
  --ink:#1f1f1f;
  --text:#555555;
  --muted:#8a8a8a;
  --line:#e3e3e3;
  --grey-circle:#6e6e6e;
  --grey-light:#b9b9b9;
  --white:#ffffff;
  --black:#111111;
  --footer-bar:#3b3b3b;
}
*{box-sizing:border-box;margin:0;padding:0}
html,body{width:1200px;height:3327px;overflow:hidden}
body{font-family:'Lato',sans-serif;color:var(--ink);background:var(--white);position:relative}
section,header,footer{position:absolute;left:0;width:1200px}

/* header */
.site-header{top:0;height:122px;background:var(--white)}
.brand{position:absolute;left:85px;top:40px;display:flex;align-items:center;gap:10px}
.brand-mark{width:26px;height:26px;background:var(--gold)}
.brand-name{font-size:21px;font-weight:700;color:var(--ink);letter-spacing:.3px}
.main-nav{position:absolute;left:407px;top:60px;display:flex;gap:28px;font-size:15px;color:#666}
.main-nav .active{color:var(--ink)}
.search-icon{position:absolute;left:1080px;top:58px}

/* hero */
.hero{top:122px;height:519px}
.hero-photo{position:absolute;inset:0;background:linear-gradient(100deg,#7a705f 0%,#a39884 35%,#d8c3b2 60%,#b6a593 85%,#8b7f6f 100%)}
.hero-box{position:absolute;left:70px;top:123px;width:507px;height:257px;border:3px solid var(--white);background:rgba(60,50,40,.35);padding:36px 0 0 56px;color:var(--white)}
.hero-kicker{font-size:30px;font-weight:400;letter-spacing:.3px}
.hero-title{font-size:38px;font-weight:700;line-height:48px;margin-top:6px}
.btn-gold{display:inline-block;background:var(--gold);color:var(--white);font-size:16px;text-align:center}
.hero-box .btn-gold{position:absolute;left:62px;top:183px;width:157px;height:42px;line-height:42px}
.hero-dots{position:absolute;left:552px;top:484px;display:flex;gap:10px}
.hero-dots span{width:11px;height:11px;border-radius:50%;background:rgba(255,255,255,.55)}
.hero-dots span:first-child{background:var(--white)}

/* about */
.about{top:641px;height:399px}
.about-bg{position:absolute;inset:0;background:linear-gradient(180deg,#f4f4f4 0%,#e2e2e2 55%,#d6d6d6 100%)}
.about-mark{position:absolute;left:585px;top:30px;width:30px;height:30px;background:var(--gold)}
.section-title{position:absolute;left:0;width:100%;text-align:center;font-weight:400;color:var(--ink)}
.about .section-title{top:88px;font-size:34px}
.about-text{position:absolute;left:0;width:100%;top:154px;text-align:center;font-size:17px;color:var(--text);line-height:27px}
.about-text p+p{margin-top:14px}
.btn-black{position:absolute;left:538px;top:287px;width:168px;height:47px;line-height:47px;text-align:center;background:var(--black);color:var(--white);font-size:16px}

/* why we are */
.why{top:1040px;height:473px}
.why .section-title{top:48px;font-size:28px}
.pillars{position:absolute;left:153px;top:1098px;top:98px;display:flex;gap:5px}
.pillar{width:302px;height:302px;border-radius:50%;border:2px solid #bdbdbd;display:flex;align-items:center;justify-content:center}
.pillar-core{width:272px;height:272px;border-radius:50%;display:flex;flex-direction:column;align-items:center;justify-content:center;color:var(--white);text-align:center}
.pillar--mission .pillar-core{background:var(--grey-circle)}
.pillar--donate .pillar-core{background:var(--gold)}
.pillar--treatment .pillar-core{background:var(--grey-light)}
.pillar-title{font-size:22px;font-weight:400;margin-top:14px}
.pillar-text{font-size:12px;line-height:17px;width:170px;margin-top:6px;opacity:.9}

/* success */
.story{top:1513px;height:452px}
.story-photo{position:absolute;inset:0;background:linear-gradient(90deg,#a88f82 0%,#8f6a62 30%,#6e3d37 60%,#5c2e2b 100%)}
.story .section-title{top:102px;font-size:32px;color:var(--white)}
.story-quote{position:absolute;left:0;width:100%;top:168px;text-align:center;font-style:italic;font-size:20px;line-height:35px;color:#f1e9e7}
.story-arrow{position:absolute;top:190px}
.story-avatars{position:absolute;left:474px;top:293px;display:flex;gap:10px}
.story-avatars span{width:52px;height:52px;border-radius:50%;border:3px solid var(--white);background:#b8aaa4}
.story-avatars span:nth-child(2){background:#9b918c}
.story-avatars span:nth-child(3){background:#a9a19d}
.story-avatars span:nth-child(4){background:#c2b9b4}

/* stars */
.stars{top:1965px;height:490px}
.stars .section-title{top:76px;font-size:30px}
.star-cards{position:absolute;left:85px;top:137px;display:flex;gap:18px}
.star-card{width:333px}
.star-name{height:58px;line-height:58px;background:#2a2a2a;color:var(--white);text-align:center;font-size:22px}
.star-photo{height:272px;position:relative}
.star-photo--one{background:linear-gradient(135deg,#c6d4de,#e9e3df 55%,#d4c3b6)}
.star-photo--two{background:linear-gradient(160deg,#5d5b56,#3d3b37);display:flex;flex-direction:column;align-items:center;justify-content:center}
.star-photo--three{background:linear-gradient(135deg,#d9c7be,#efd7cf 50%,#b87c8a)}
.star-blurb{color:var(--white);font-size:15px;line-height:25px;text-align:center;width:270px}
.star-photo--two .btn-gold{width:133px;height:30px;line-height:30px;font-size:12px;font-weight:700;margin-top:14px}

/* blogs + signup */
.panels{top:2472px;height:356px}
.panel{position:absolute;top:0;height:354px;border:3px solid var(--line);padding:36px 0 0 36px}
.panel--blogs{left:85px;width:507px}
.panel--signup{left:607px;width:510px;padding-left:30px}
.panel-title{font-size:22px;font-weight:300;color:#333;letter-spacing:.5px}
.post{position:absolute;left:36px;display:flex;gap:24px}
.post-date{width:82px;text-align:center}
.post-day{height:52px;line-height:52px;background:#d4d4d4;color:var(--white);font-size:32px}
.post-month{height:30px;line-height:30px;background:#8f8f8f;color:var(--white);font-size:15px}
.post-title{font-size:16px;color:#222;margin-top:4px}
.post-excerpt{font-size:11px;color:var(--muted);line-height:16px;width:320px;margin-top:8px}
.post-more{font-size:12px;color:#555;margin-top:18px}
.signup-title{font-size:20px;font-weight:700;color:#333}
.signup-sub{font-size:13px;color:var(--muted);margin-top:14px}
.field{width:425px;height:42px;border:1px solid #cfcfcf;font-size:13px;color:#666;padding-left:14px;line-height:40px;margin-top:7px}
.field:first-of-type{margin-top:21px}
.panel--signup .btn-gold{width:165px;height:43px;line-height:43px;font-size:13px;font-weight:700;margin-top:10px}

/* footer */
.site-footer{top:2828px;height:499px}
.footer-scene{position:absolute;left:0;top:0;width:1200px;height:432px;background:linear-gradient(180deg,#9a9a9a 0%,#6d6d6d 35%,#4e4e4e 70%,#404040 100%)}
.footer-col{position:absolute;top:160px;color:var(--white)}
.footer-col h3{font-size:22px;font-weight:400;letter-spacing:.3px}
.footer-col ul{list-style:none;margin-top:20px}
.footer-col li{font-size:15px;line-height:35px;color:#eee}
.footer-divider{position:absolute;top:157px;width:1px;height:190px;background:rgba(255,255,255,.35)}
.socials{display:flex;gap:8px;margin-top:12px}
.socials span{width:46px;height:46px;border-radius:50%;border:2px solid var(--white)}
.footer-bar{position:absolute;left:0;top:432px;width:1200px;height:67px;background:var(--footer-bar);color:#d0d0d0;text-align:center;font-size:14px;line-height:67px}
</style>
</head>
<body>

<header class="site-header">
  <div class="brand"><span class="brand-mark"></span><span class="brand-name">Bramble Harbor Foundation</span></div>
  <nav class="main-nav">
    <span class="active">HOME</span><span>ABOUT US</span><span>WHAT WE DO</span><span>SERVICES</span><span>TESTIMONIAL</span><span>CONTACT</span>
  </nav>
  <svg class="search-icon" width="20" height="20" viewBox="0 0 20 20" aria-hidden="true"><circle cx="8" cy="8" r="6" fill="none" stroke="#333" stroke-width="2.2"/><line x1="12.5" y1="12.5" x2="18" y2="18" stroke="#333" stroke-width="2.4"/></svg>
</header>

<section class="hero">
  <div class="hero-photo" role="img" aria-label="Photo of a smiling child patient outdoors in warm light"></div>
  <div class="hero-box">
    <p class="hero-kicker">WE HELP CANCER PATIENTS</p>
    <h1 class="hero-title">FINANCIALLY FOR<br>THIER TREATMENT</h1>
    <span class="btn-gold">Learn More</span>
  </div>
  <div class="hero-dots"><span></span><span></span><span></span><span></span></div>
</section>

<section class="about">
  <div class="about-bg" role="img" aria-label="Soft grey misty mountain landscape"></div>
  <div class="about-mark"></div>
  <h2 class="section-title">ABOUT US</h2>
  <div class="about-text">
    <p>Vivamus porttitor purus nisi eleifend libero a tempus libero lectus</p>
    <p>mollis aliquam Curabitur iaculis tempus eros Curabitur vel mi sit amet magna malesuada ultrices<br>Ut nisi erat fermentum vel congue id euismod in elit Fusce ultricies orci ac feugiat</p>
  </div>
  <span class="btn-black">Learn More</span>
</section>

<section class="why">
  <h2 class="section-title">WHY WE ARE</h2>
  <div class="pillars">
    <div class="pillar pillar--mission"><div class="pillar-core">
      <svg width="66" height="52" viewBox="0 0 66 52" fill="none" stroke="#fff" stroke-width="2.5" aria-hidden="true"><rect x="6" y="20" width="54" height="12" rx="3"/><circle cx="16" cy="13" r="5"/><line x1="12" y1="32" x2="12" y2="44"/><line x1="54" y1="32" x2="54" y2="44"/><circle cx="12" cy="47" r="3"/><circle cx="54" cy="47" r="3"/></svg>
      <h3 class="pillar-title">OUR MISSION</h3>
      <p class="pillar-text">Ut nisi erat fermentum vel congue id euismod in elit</p>
    </div></div>
    <div class="pillar pillar--donate"><div class="pillar-core">
      <svg width="66" height="52" viewBox="0 0 66 52" fill="none" stroke="#fff" stroke-width="2.5" aria-hidden="true"><path d="M4 34h12l14 6h16l14-10"/><path d="M16 34l10-6h14"/><circle cx="40" cy="10" r="6"/><circle cx="50" cy="20" r="4"/></svg>
      <h3 class="pillar-title">DONATE NOW</h3>
      <p class="pillar-text">Ut nisi erat fermentum vel congue id euismod in elit</p>
    </div></div>
    <div class="pillar pillar--treatment"><div class="pillar-core">
      <svg width="60" height="56" viewBox="0 0 60 56" fill="none" stroke="#fff" stroke-width="2.5" aria-hidden="true"><rect x="18" y="14" width="14" height="32" rx="2" transform="rotate(45 25 30)"/><line x1="40" y1="14" x2="50" y2="4"/><line x1="45" y1="2" x2="54" y2="11"/><line x1="14" y1="42" x2="6" y2="50"/></svg>
      <h3 class="pillar-title">TREATMENT</h3>
      <p class="pillar-text">Ut nisi erat fermentum vel congue id euismod in elit</p>
    </div></div>
  </div>
</section>

<section class="story">
  <div class="story-photo" role="img" aria-label="Photo of a smiling girl in a headscarf against a deep red backdrop"></div>
  <h2 class="section-title">SUCCESS STORY</h2>
  <p class="story-quote">“Morbi diam mauris viverra in gravida eu mattis in ante Morbi eget arcu Morbi<br>porta libero id ullamcorper nonummy nibh ligula pulvinar metus eget<br>consectetuer augue nisi quis ”</p>
  <svg class="story-arrow" style="left:145px" width="24" height="60" viewBox="0 0 24 60" aria-hidden="true"><polyline points="22,2 2,30 22,58" fill="none" stroke="#fff" stroke-width="2"/></svg>
  <svg class="story-arrow" style="left:1010px" width="24" height="60" viewBox="0 0 24 60" aria-hidden="true"><polyline points="2,2 22,30 2,58" fill="none" stroke="#fff" stroke-width="2"/></svg>
  <div class="story-avatars">
    <span role="img" aria-label="Patient portrait"></span><span role="img" aria-label="Patient portrait"></span><span role="img" aria-label="Patient portrait"></span><span role="img" aria-label="Patient portrait"></span>
  </div>
</section>

<section class="stars">
  <h2 class="section-title">OUR STARS</h2>
  <div class="star-cards">
    <article class="star-card">
      <h3 class="star-name">Patient Name</h3>
      <div class="star-photo star-photo--one" role="img" aria-label="Photo of a woman in a blue headscarf resting on a pillow"></div>
    </article>
    <article class="star-card">
      <h3 class="star-name">Patient Name</h3>
      <div class="star-photo star-photo--two">
        <p class="star-blurb">Ut nisi erat fermentum vel congue id euismod in elit Fusce ultricies orci ac feugiat suscipit leo massa sodales velit et scelerisque mi tortor at i</p>
        <span class="btn-gold">READ MORE</span>
      </div>
    </article>
    <article class="star-card">
      <h3 class="star-name">Patient Name</h3>
      <div class="star-photo star-photo--three" role="img" aria-label="Photo of a young child patient among pink flowers"></div>
    </article>
  </div>
</section>

<section class="panels">
  <div class="panel panel--blogs">
    <h3 class="panel-title">RECENT&nbsp; BLOGS</h3>
    <div class="post" style="top:83px">
      <div class="post-date"><div class="post-day">02</div><div class="post-month">OCT</div></div>
      <div><h4 class="post-title">Etiam eu urna Sed porta Suspe</h4><p class="post-excerpt">netus et malesuada fames ac turpis egestas Cras id elit integer apibus malesuada fringilla eu condimentum</p><p class="post-more">READ MORE</p></div>
    </div>
    <div class="post" style="top:216px">
      <div class="post-date"><div class="post-day">08</div><div class="post-month">OCT</div></div>
      <div><h4 class="post-title">Ut nisi erat fermentum vel congue</h4><p class="post-excerpt">netus et malesuada fames ac turpis egestas Cras id elit integer apibus malesuada fringilla eu condimentum</p><p class="post-more">READ MORE</p></div>
    </div>
  </div>
  <div class="panel panel--signup">
    <h3 class="signup-title">SIGN UP HERE FOR ANY HELP</h3>
    <p class="signup-sub">netus et malesuada fames ac turpis egestas Cras id</p>
    <div class="field">First Name</div>
    <div class="field">Last Name</div>
    <div class="field">Email address</div>
    <span class="btn-gold">SUBSCRIBE</span>
  </div>
</section>

<footer class="site-footer">
  <div class="footer-scene" role="img" aria-label="Grey layered mountain range silhouette"></div>
  <div class="footer-col" style="left:116px"><h3>QUICK LINKS</h3><ul><li>Home</li><li>About Us</li><li>What We Do</li><li>Why Us</li></ul></div>
  <div class="footer-divider" style="left:305px"></div>
  <div class="footer-col" style="left:364px"><h3>SUBLINKS</h3><ul><li>Cancer Patients</li><li>Donate Now</li><li>Success Stories</li><li>Blogs</li></ul></div>
  <div class="footer-divider" style="left:553px"></div>
  <div class="footer-col" style="left:632px"><h3>RESOURCES</h3><ul><li>Sitemap</li><li>Term of Use</li><li>Contact Us</li></ul></div>
  <div class="footer-divider" style="left:808px"></div>
  <div class="footer-col" style="left:870px"><h3>FOLLOW US</h3><div class="socials"><span></span><span></span><span></span><span></span></div></div>
  <div class="footer-bar">© 2017 Company Name &nbsp;All right reserved &nbsp;Term of Use</div>
</footer>

</body>
</html>
```